7 3/4 x 5 1/4 Annual Banquet Invitation

Design an invitation for our Chamber's annual banquet. It will be a single sided invitation 5 1/4" wide by 7 3/4" height that we will print in-house. Our logo is attached. The theme is "Serving Together". I was thinking of an image with two hands coming together in a handshake, perhaps intertwining our logo colors. This is just a thought. I am open for any suggestions! Text for the invitation should be as follows: The Board of Directors and Staff cordially invites you to attend the 81st Annual Gathering & Mini-Trade Showcase - Monday, January 22, 2018. 5:30 p.m. Social, 6:00 p.m. Dinner. Ashgrove Chapel, 4918 Colton R. Pike Rd S, Maplebrook. Please RSVP by January 18, 2018.

Target Market(s)

This invitation will be printed and mailed to our membership.

Industry/Entity Type

Business Management

Colors
33a6d7
faa54b
0355a3
00a990

Requirements
Must have
• Event info as indentified above.
Nice to have
• Our Logo

```html
<!DOCTYPE html>
<html lang="en">
<head>
<meta charset="utf-8">
<title>Serving Together – Annual Banquet Invitation</title>
<link rel="stylesheet" href="https://fonts.googleapis.com/css2?family=Gelasio:wght@400&family=Source+Sans+3:wght@400;600&display=swap">
<style>
  :root {
    --navy: #283a8f;
    --sky: #22a7e0;
    --grey-text: #6d6e71;
    --orange: #f7a541;
    --paper: #ffffff;
    --photo-light: #dfe3e8;
    --photo-mid: #8a8f96;
    --photo-dark: #2c2e33;
  }
  * { margin: 0; padding: 0; box-sizing: border-box; }
  html, body { width: 943px; height: 1200px; overflow: hidden; background: var(--paper); }
  .invitation {
    position: relative;
    width: 943px;
    height: 1200px;
    background: var(--paper);
    font-family: "Source Sans 3", sans-serif;
    color: var(--grey-text);
  }
  .shapes { position: absolute; inset: 0; width: 943px; height: 1200px; }
  .headline {
    position: absolute;
    left: 37px;
    font-family: "Gelasio", serif;
    font-weight: 400;
    font-size: 66px;
    line-height: 1;
    color: var(--paper);
    letter-spacing: 0.5px;
  }
  .headline--serving { top: 285px; }
  .headline--together { top: 410px; }
  .text-block { position: absolute; left: 37px; }
  .invite-line { top: 542px; font-size: 29px; line-height: 36px; }
  .event-date {
    top: 690px;
    font-family: "Gelasio", serif;
    font-size: 34px;
    line-height: 40px;
    color: var(--navy);
  }
  .event-times {
    top: 733px;
    font-size: 29px;
    line-height: 34px;
    color: var(--navy);
  }
  .divider {
    position: absolute;
    left: 37px;
    width: 430px;
    height: 2px;
    background: var(--orange);
  }
  .divider--first { top: 794px; }
  .divider--second { top: 930px; }
  .venue { top: 822px; font-size: 29px; line-height: 44px; }
  .rsvp { top: 956px; font-size: 29px; line-height: 34px; }
  .organiser {
    position: absolute;
    left: 37px;
    top: 1118px;
    display: flex;
    align-items: center;
    gap: 12px;
  }
  .organiser-dot {
    width: 30px;
    height: 30px;
    border-radius: 50%;
    background: var(--sky);
  }
  .organiser-name {
    font-family: "Source Sans 3", sans-serif;
    font-weight: 600;
    font-size: 20px;
    line-height: 22px;
    color: var(--navy);
  }
  .website {
    position: absolute;
    right: 30px;
    top: 1145px;
    font-size: 22px;
    color: var(--paper);
  }
</style>
</head>
<body>
<main class="invitation">
  <svg class="shapes" viewBox="0 0 788 1162" preserveAspectRatio="none">
    <defs>
      <linearGradient id="photoTone" x1="0" y1="0" x2="1" y2="1">
        <stop offset="0" stop-color="var(--photo-light)"/>
        <stop offset="0.45" stop-color="var(--photo-mid)"/>
        <stop offset="1" stop-color="var(--photo-dark)"/>
      </linearGradient>
    </defs>
    <polygon class="handshake-photo" role="img" aria-label="Photo of a businessman in a dark suit extending his hand for a handshake" points="118,0 788,0 788,523 705,673" fill="url(#photoTone)"/>
    <polygon class="accent-triangle" points="788,523 788,1162 438,1162" fill="var(--sky)"/>
    <polygon class="banner" points="2,250 576,250 520,363 2,363" fill="var(--navy)"/>
    <polygon class="banner" points="2,374 440,374 383,486 2,486" fill="var(--navy)"/>
  </svg>

  <h1 class="headline headline--serving">SERVING</h1>
  <h1 class="headline headline--together">TOGETHER</h1>

  <p class="text-block invite-line">The Board of Directors and Staff cordially<br>invites you to attend the<br>81st Annual Gathering &amp; Mini-Trade Showcase</p>

  <p class="text-block event-date">Monday, January 22, 2018. 5:30 p.m.</p>
  <p class="text-block event-times">Social, 6:00 p.m. Dinner.</p>

  <div class="divider divider--first"></div>
  <p class="text-block venue">Ashgrove Chapel, 4918 Colton R.<br>Pike Rd S, Maplebrook.</p>
  <div class="divider divider--second"></div>

  <p class="text-block rsvp">Please RSVP by January 18, 2018.</p>

  <div class="organiser">
    <span class="organiser-dot"></span>
    <p class="organiser-name">HARBOR CREEK CHAMBER<br>OF COMMERCE &amp; TOURISM</p>
  </div>

  <p class="website">theharborcreekchamber.com</p>
</main>
</body>
</html>
```